Brochure Design Project (Design Studio)

Items required:
1-Brochure. We suggest 15Cm X 15 Cm after cutting.
2-Business Card.
3-Head letter.
4-Folder ( folder should carry the Brochure in pocket and the business card in a pocket on the opposite side of the folder.
5-Envelope to carry everything.
This brochure is expected to draw attention of high level management in companies to the quality and creativity of the design work and encourage them to do business with us. note that brochure will be printed in high quality printing and paper.
The game plan is as follows:
Over all description, the theme of the brochure is drawn from the website theme (website will be uploaded shortly, pictures of the website are attached, logo appears in the top left corner). Please avoid direct copying from the website unless it is a creative copying, just draw the theme from there. however, we need it to be elegant, stylish and class in colors and style. This is a MUST.
Furthermore, the main items of the Brochure:
1-The Studio is not just a studio: we will take about how Branding. A file is attached of the content. (slight changes/modification can apply during the designing process)
2-The Process: this one has to be a visual illustration of the process, it has to be very creative, could be elegant arrows and comics, could be elegant drawing, could be an elegant icons. The drawing should be separate from the steps, we need to the drawing and we need to have the steps listed and commentary, or if want to integrate both in one in an artistic way. Just don’t lose track of the theme and elegance. (steps and commentary are attached, slight changes/modification can apply at anytime.
3-Our Team: another drawing of your suggestion to illustrate the team members, we need to include the names and designation as well leave a place for some of them to say what they need to say about their style of designing. I leave it for your imagination to put this all together in a nice attractive visual illustration.
4-Works: this section will generally show the works of our designers. It needs to be focused on the works themselves, client should be able to view the details of the works ( note that when it comes to brochures and websites, we don’t need to reach to the extent with which the client can read the text in those pictures of the website or brochure, but still can see the overall design clearly). Each design is to carry the name of the designer. Last thing, this section will classify works into categories, like, Brochures, Corporate identity, print design. We didn’t finalize those categories, we will provide them to you shortly, last thing to be said, we are planning to include around 25-30 designs of each sub-category, eg. Corporate identity will have 30 business card s designs and 30 stationary designs.
5-Contacts: the company contacts.
We the brochure after printing should be 15x15 Cm.
Creativity and art work is a major player in selection.
general managers, owners
Printing

```html
<!DOCTYPE html>
<html lang="en">
<head>
<meta charset="utf-8">
<title>Calvera Studio – Branding Brochure Spread</title>
<link rel="stylesheet" href="https://fonts.googleapis.com/css2?family=Jost:ital,wght@0,300;0,400;1,400&family=Oswald:wght@400&display=swap">
<style>
  :root {
    --page-bg: #efefef;
    --board: #ffffff;
    --wine: #6c0504;
    --wine-deep: #5e0302;
    --crimson: #d2122e;
    --slate: #5b5b5b;
    --ink-grey: #4a5560;
    --accent-green: #8cc63f;
    --lime: #c9f31d;
    --white: #ffffff;
  }
  * { margin: 0; padding: 0; box-sizing: border-box; }
  html, body { width: 1200px; height: 651px; overflow: hidden; }
  body { background: var(--page-bg); position: relative; font-family: "Jost", Arial, sans-serif; }

  .spread-board {
    position: absolute; left: 66px; top: 55px; width: 1075px; height: 545px;
    background: var(--board); box-shadow: 0 6px 22px rgba(0,0,0,.22);
  }

  .page { position: absolute; top: 77px; width: 510px; height: 510px; overflow: hidden; }
  .page--cover { left: 72px; border: 1px solid #bbb; }
  .page--branding { left: 621px; background: var(--wine); border: 1px solid #aaa; }

  /* cover */
  .cover-visual {
    position: absolute; left: 0; top: 0; width: 100%; height: 320px;
    background: radial-gradient(ellipse at 30% 40%, #c8102e 0 18%, transparent 40%),
                radial-gradient(ellipse at 65% 45%, #b50d2a 0 20%, transparent 45%),
                linear-gradient(90deg, #c9cfcf, #e6e6e2 60%, #f4f3f0);
  }
  .cover-brandbar {
    position: absolute; left: 0; top: 320px; width: 100%; height: 55px; background: var(--white);
    display: flex; align-items: center; justify-content: center; gap: 10px;
  }
  .brand-name { font-family: "Jost", Arial, sans-serif; font-weight: 300; font-size: 26px; color: var(--ink-grey); letter-spacing: 1px; }
  .brand-dot { width: 10px; height: 10px; background: var(--accent-green); border-radius: 50%; }
  .cover-band {
    position: absolute; left: 0; top: 375px; width: 100%; height: 135px;
    background: linear-gradient(90deg, #6a0a0a, #5a5a5a);
  }
  .cover-tagline {
    position: absolute; right: 18px; bottom: 14px; color: var(--white);
    font-weight: 300; font-size: 24px;
  }

  /* branding page */
  .top-strip { position: absolute; left: 0; top: 0; width: 100%; height: 8px; background: var(--wine-deep); }
  .page-header {
    position: absolute; left: 0; top: 8px; width: 100%; height: 55px; background: var(--white);
    display: flex; align-items: center; justify-content: flex-end; gap: 10px; padding-right: 20px;
  }
  .page-header .brand-name { font-size: 24px; }
  .section-tag {
    position: absolute; left: 12px; top: 20px; width: 118px; height: 36px;
    background: linear-gradient(180deg, #8b1a1a, #5b0606); color: var(--white);
    font-size: 20px; font-weight: 300; line-height: 36px; text-align: center;
    transform: rotate(-12deg); box-shadow: 2px 3px 6px rgba(0,0,0,.4); border: 1px solid #ddd;
  }
  .intro-copy {
    position: absolute; left: 14px; top: 92px; width: 484px;
    color: var(--white); font-size: 11.6px; line-height: 17px;
  }
  .intro-copy .highlight { color: var(--crimson); }

  .benefit-block { position: absolute; top: 305px; color: var(--white); }
  .benefit-block--strong { left: 12px; width: 240px; }
  .benefit-block--gives { left: 262px; width: 240px; }
  .benefit-title { font-family: "Oswald", Arial, sans-serif; color: var(--crimson); font-size: 21px; line-height: 24px; }
  .benefit-sub { font-family: "Oswald", Arial, sans-serif; color: var(--crimson); font-size: 14px; line-height: 16px; }
  .benefit-list { list-style: none; margin-top: 6px; font-size: 11.6px; line-height: 20.5px; }
  .benefit-list li::before { content: "•"; margin-right: 6px; }
  .benefit-block--gives .benefit-list { margin-top: 4px; }
  .curve-arrow { position: absolute; width: 70px; height: 80px; }
  .curve-arrow--strong { left: 148px; top: 315px; }
  .curve-arrow--gives { left: 420px; top: 315px; }

  .closing-line {
    position: absolute; left: 14px; top: 445px; width: 490px;
    color: var(--lime); font-style: italic; font-size: 17px; line-height: 22px;
  }
</style>
</head>
<body>
  <div class="spread-board"></div>

  <section class="page page--cover">
    <div class="cover-visual" role="img" aria-label="Fashion photograph: a woman in a flowing red gown dissolving into red paint splashes against a pale grey wall"></div>
    <div class="cover-brandbar">
      <span class="brand-name">Calvera Studio</span>
      <span class="brand-dot"></span>
    </div>
    <div class="cover-band">
      <p class="cover-tagline">Personify your business</p>
    </div>
  </section>

  <section class="page page--branding">
    <div class="top-strip"></div>
    <header class="page-header">
      <span class="brand-name">Calvera Studio</span>
      <span class="brand-dot"></span>
    </header>
    <div class="section-tag">Branding!</div>

    <div class="intro-copy">
      <p>Do you prefer to work with specific Individuals over others? Do you feel that working with those individuals give you the peace of mind because you know that they are Enthusiastic, ethical, Goal Focused, Committed, Disciplined, creative, visionary and self-aware?</p>
      <p>Well, probably you like to work with companies of the same qualities as those persons!</p>
      <p>COMPANIES HAVE PERSONALITIES TOO.</p>
      <p>Branding is your vehicle to deliver the traits of your company to the audience. Branding assist you to control the perception of company among public.</p>
      <p>If you are very organized company, deliver on time, committed to your clients, produce quality products to the highest standards. <span class="highlight">Branding is the key to make the public hear and believe those qualities and consider your products as their 1st choice.</span></p>
    </div>

    <div class="benefit-block benefit-block--strong">
      <h2 class="benefit-title">Strong Branding</h2>
      <p class="benefit-sub">Means your company is:</p>
      <ul class="benefit-list">
        <li>Large and established.</li>
        <li>A synonym of Quality.</li>
        <li>Experienced and reliable.</li>
      </ul>
    </div>
    <svg class="curve-arrow curve-arrow--strong" viewBox="0 0 70 80" aria-hidden="true">
      <path d="M10 8 C50 8 66 32 58 62 L66 62 L50 78 L36 58 L44 60 C50 36 40 22 10 24 Z" fill="#6a6a6a" stroke="#fff" stroke-width="3" stroke-linejoin="round"/>
    </svg>

    <div class="benefit-block benefit-block--gives">
      <h2 class="benefit-title">Branding gives you:</h2>
      <ul class="benefit-list">
        <li>Loyalty and advocacy.</li>
        <li>Influence of choice.</li>
        <li>Command a price premium.</li>
        <li>Uniqueness.</li>
        <li>Growth of your business and products.</li>
      </ul>
    </div>
    <svg class="curve-arrow curve-arrow--gives" viewBox="0 0 70 80" aria-hidden="true">
      <path d="M10 8 C50 8 66 32 58 62 L66 62 L50 78 L36 58 L44 60 C50 36 40 22 10 24 Z" fill="#6a6a6a" stroke="#fff" stroke-width="3" stroke-linejoin="round"/>
    </svg>

    <p class="closing-line">We are more than just a creative studio; we can personify your business and dress to impress!</p>
  </section>
</body>
</html>
```